Brindlewood Holdings LLC - Business Cards

Need the following information on the cards:

Name: Marcus T Velding
Title: Chief Executive Manager

Business address:
412 N Pickerel Ridge Road #118
Larkfield, Il 60999

Phone: (555) 481-0362 - Business
BRX FFL license number: 5-81-xxx-xx-xx-04519
Email: marcus.velding@brindlewoodholdingsffl.example

Target Market(s)

Firearm owners

Industry/Entity Type

Firearms industry,

Contact Information for Business Card

Contact number, name and title, web page address, email, business address and brx license number,

Requirements
Must have
• Name, title, business address, phone numbers, BRX license numbers, web page address and email address.
Nice to have
• Cellphone number,

```html
<!DOCTYPE html>
<html lang="en">
<head>
<meta charset="utf-8">
<title>Brindlewood Holdings LLC – Business Cards</title>
<link href="https://fonts.googleapis.com/css2?family=Poppins:wght@400;500;600;700&display=swap" rel="stylesheet">
<style>
  :root {
    --bg: #e4e4e4;
    --paper: #ffffff;
    --ink: #231f20;
    --red: #d71f26;
    --text-light: #f4f4f4;
    --shadow: rgba(0,0,0,0.18);
  }
  * { margin: 0; padding: 0; box-sizing: border-box; }
  html, body { width: 1200px; height: 800px; overflow: hidden; }
  body {
    background: var(--bg);
    font-family: "Poppins", sans-serif;
    position: relative;
  }
  .sheet-heading { position: absolute; top: 28px; right: 60px; text-align: right; }
  .sheet-heading h1 { color: var(--red); font-size: 30px; font-weight: 600; line-height: 1.1; }
  .sheet-heading p { color: var(--ink); font-size: 12px; font-weight: 500; margin-top: 8px; }

  .card {
    position: absolute; width: 560px; height: 320px;
    box-shadow: 0 10px 24px var(--shadow);
    overflow: hidden;
  }
  /* Front */
  .card-front { left: 60px; top: 110px; background: var(--paper); }
  .brand-mark {
    display: flex; flex-direction: column; align-items: center;
    color: var(--red); font-weight: 700; text-transform: uppercase; line-height: 1.05;
    white-space: nowrap;
  }
  .brand-mark .dot { width: 14px; height: 14px; border-radius: 50%; background: var(--red); margin-bottom: 10px; }
  .card-front .brand-mark { position: absolute; left: 0; right: 0; top: 92px; font-size: 34px; letter-spacing: 1px; }
  .card-front .brand-mark small { font-size: 14px; letter-spacing: 4px; margin-top: 6px; }
  .card-front .web-address {
    position: absolute; left: 0; right: 0; top: 232px; text-align: center;
    font-size: 17px; letter-spacing: 1.5px; color: var(--red);
  }
  .card-front .web-address span { color: var(--ink); }

  /* Back */
  .card-back { left: 580px; top: 440px; background: var(--paper); }
  .card-back .panel { position: absolute; inset: 0; }
  .person { position: absolute; left: 30px; top: 24px; }
  .person .name { color: var(--text-light); font-size: 24px; font-weight: 500; }
  .person .title { color: var(--red); font-size: 13px; margin-top: -2px; }
  .contact-list { position: absolute; left: 30px; top: 96px; list-style: none; }
  .contact-list li {
    display: flex; align-items: flex-start; gap: 10px;
    color: var(--text-light); font-size: 12px; line-height: 1.35; margin-bottom: 5px;
    white-space: nowrap;
  }
  .contact-list svg { width: 12px; height: 12px; flex: none; margin-top: 3px; fill: var(--red); }
  .licence {
    position: absolute; left: 30px; top: 264px;
    color: #fff; font-size: 12.5px; font-weight: 600; white-space: nowrap;
  }
  .licence span { font-weight: 400; }
  .card-back .brand-mark {
    position: absolute; right: 8px; top: 128px; width: 140px;
    font-size: 17px; text-align: center;
  }
  .card-back .brand-mark small { font-size: 8px; letter-spacing: 2px; margin-top: 4px; }
</style>
</head>
<body>
  <header class="sheet-heading">
    <h1>Business Card- Mockup 1</h1>
    <p>100% Editable &nbsp;|&nbsp; Vector Design &nbsp;|&nbsp;Print Ready &nbsp;|&nbsp; CMYK color mode</p>
  </header>

  <section class="card card-front" aria-label="Business card front">
    <div class="brand-mark">
      <span class="dot"></span>
      Brindlewood
      <small>Holdings LLC</small>
    </div>
    <p class="web-address"><span>www.</span>brindlewoodholdingsffl.example</p>
  </section>

  <section class="card card-back" aria-label="Business card back">
    <svg class="panel" viewBox="0 0 560 320" aria-hidden="true">
      <defs>
        <linearGradient id="darkPanel" x1="0" y1="0" x2="1" y2="1">
          <stop offset="0" stop-color="#2b2829"/>
          <stop offset="1" stop-color="#1c1a1b"/>
        </linearGradient>
      </defs>
      <polygon points="0,0 420,0 376,286 356,320 0,320" fill="#d71f26"/>
      <polygon points="0,0 410,0 366,286 346,320 0,320" fill="url(#darkPanel)"/>
      <polygon points="0,252 372,252 367,280 348,296 0,296" fill="#d71f26"/>
    </svg>

    <div class="person">
      <p class="name">Marcus T Velding</p>
      <p class="title">Chief Executive Manager</p>
    </div>

    <ul class="contact-list">
      <li><svg viewBox="0 0 24 24"><path d="M6.6 10.8a15 15 0 0 0 6.6 6.6l2.2-2.2c.3-.3.7-.4 1-.2 1.1.4 2.3.6 3.6.6.6 0 1 .4 1 1V20c0 .6-.4 1-1 1A17 17 0 0 1 3 4c0-.6.4-1 1-1h3.5c.6 0 1 .4 1 1 0 1.3.2 2.5.6 3.6.1.3 0 .7-.2 1z"/></svg>(555) 481-0362</li>
      <li><svg viewBox="0 0 24 24"><path d="M7 1h10a2 2 0 0 1 2 2v18a2 2 0 0 1-2 2H7a2 2 0 0 1-2-2V3a2 2 0 0 1 2-2zm0 3v14h10V4z"/></svg>55 - 5012 - 3478</li>
      <li><svg viewBox="0 0 24 24"><path d="M2 5h20v14H2zm2 2v.5l8 5 8-5V7zm0 2.8V17h16V9.8l-8 5z"/></svg>marcus.velding@brindlewoodholdingsffl.example</li>
      <li><svg viewBox="0 0 24 24"><path d="M12 2a10 10 0 1 0 0 20 10 10 0 0 0 0-20zm-1 2.1V8H7.3A8 8 0 0 1 11 4.1zM13 4.1A8 8 0 0 1 16.7 8H13zM4.3 10H11v4H4.3a8 8 0 0 1 0-4zm8.7 0h6.7a8 8 0 0 1 0 4H13zm-5.7 6H11v3.9A8 8 0 0 1 7.3 16zm5.7 0h3.7a8 8 0 0 1-3.7 3.9z"/></svg>www.brindlewoodholdingsffl.example</li>
      <li><svg viewBox="0 0 24 24"><path d="M12 2a7 7 0 0 0-7 7c0 5 7 13 7 13s7-8 7-13a7 7 0 0 0-7-7zm0 9.5a2.5 2.5 0 1 1 0-5 2.5 2.5 0 0 1 0 5z"/></svg><span>412 N Pickerel Ridge Road #118<br>Larkfield, Il 60999</span></li>
    </ul>

    <p class="licence">BRX FFL License Number : <span>5-81-xxx-xx-xx-04519</span></p>

    <div class="brand-mark">
      <span class="dot"></span>
      Brindlewood
      <small>Holdings LLC</small>
    </div>
  </section>
</body>
</html>
```